BRAVO Nutrition Mobile Application Layout

I am looking for professional grade app page layouts to use in my clickable prototype for an investor pitch.

B.R.A.V.O. is an acronym for Balanced Responsive Vitality Assessment Optimizer.

This app is a nutrition diet generation tool for the consumer (type in profile, diet is generated).

I am most interested in several pages consisting of:
- A landing/login page
- User profile page which will consist of a visual representation of adherence to the diet such as a pie chart, bar with percentage representing said adherence, etc.
- Profile settings page
- Blank general layout page (a standard template to be used with all pages in the application)

I would prefer greens, reds, and yellows in the design
The design should reflect health and nutrition
The design should have an "ease of use appearance"

Apps that are useful to look at are:
Trimwell Buddy
Nutrilogix
Grocevane

I have uploaded a "working" logo that I am using

I look forward to seeing your talents and appreciate your work in advance!

Target Market(s)

General population - health and wellness companies

Industry/Entity Type

Health And Wellness

Font styles to use
Serif
Sans Serif
Other font styles liked:
• Dealer's Choice

Colors
9ccb3b
f04a51
fbed22

Requirements
Must have
• - A landing/login page
• - User profile page which will consist of a visual representation of adherence to the diet such as a pie chart, bar with percentage representing said adherence, etc.
• - Profile settings page
• - Blank general layout page (a standard template to be used with all pages in the application)
• The design should reflect health and nutrition
• The design should have an "ease of use appearance"
Nice to have
• Incorporating the acronym spelled out.
• Common image in the background reflecting nutrition and health.

```html
<!DOCTYPE html>
<html lang="en">
<head>
<meta charset="utf-8">
<title>BRAVO – My Profile</title>
<link href="https://fonts.googleapis.com/css2?family=Roboto:wght@400;500;700&display=swap" rel="stylesheet">
<style>
  :root {
    --status-green: #4e8a1b;
    --header-green: #5c9c20;
    --app-green: #6aae23;
    --chart-fill-top: #b6df2a;
    --chart-fill-bottom: #79b924;
    --grid-line: rgba(255,255,255,0.28);
    --white: #ffffff;
    --card-text: #555555;
    --yellow: #fcee21;
    --flag-lime: #c8f03a;
    --goal-red: #f04a51;
    --track-light: #b9ea7e;
    --protein: #d5703e;
    --carbs: #f6e51f;
    --energy: #c93aa6;
    --water: #3db4d8;
    --pie-blue: #5cc4d6;
    --pie-orange: #d6845d;
    --pie-yellow: #fbf046;
    --pie-pink: #d45cae;
    --divider: #8fc957;
  }
  html, body {
    margin: 0;
    padding: 0;
    width: 1200px;
    height: 2498px;
    overflow: hidden;
    background: var(--app-green);
    font-family: "Roboto", Arial, sans-serif;
    color: var(--white);
  }
  .screen {
    position: absolute;
    left: 0; top: 0;
    width: 640px;
    height: 1332px;
    transform: scale(1.875);
    transform-origin: 0 0;
    background: var(--app-green);
    overflow: hidden;
  }
  .abs { position: absolute; }
  .status-bar {
    left: 0; top: 0; width: 640px; height: 40px;
    background: var(--status-green);
    font-size: 20px; color: rgba(255,255,255,0.92);
  }
  .status-time { left: 0; width: 640px; top: 7px; text-align: center; }
  .status-battery-text { right: 50px; top: 7px; }
  .app-header {
    left: 0; top: 40px; width: 640px; height: 82px;
    background: var(--header-green);
  }
  .header-title {
    left: 0; width: 640px; top: 22px; text-align: center;
    font-size: 28px; font-weight: 500;
  }
  .avatar {
    left: 565px; top: 16px; width: 50px; height: 50px;
    border-radius: 50%;
    background: radial-gradient(circle at 50% 40%, #d9b7a0, #5b5148);
    box-shadow: 0 0 0 2px var(--white);
  }
  .range-select { left: 82px; top: 138px; font-size: 22px; }
  .stat-card {
    top: 545px; width: 165px; height: 108px;
    background: var(--white); border-radius: 8px;
    box-shadow: 0 0 12px rgba(220,255,160,0.85);
    color: var(--card-text); text-align: center;
  }
  .stat-value { margin-top: 14px; font-size: 38px; line-height: 44px; }
  .stat-unit { font-size: 22px; }
  .stat-label { font-size: 22px; margin-top: 4px; }
  .section-title { font-size: 24px; font-weight: 500; }
  .macro-label { font-size: 22px; }
  .macro-pct { font-size: 22px; text-align: right; width: 80px; }
  .macro-track {
    left: 40px; width: 238px; height: 7px; border-radius: 4px;
    background: var(--track-light); overflow: hidden;
  }
  .macro-fill { height: 100%; border-radius: 4px; }
  .aim-label { left: 38px; font-size: 22px; font-weight: 700; }
  .divider { left: 16px; top: 1104px; width: 608px; height: 2px; background: var(--divider); }
</style>
</head>
<body>
<main class="screen">

  <div class="abs status-bar">
    <svg class="abs" style="left:8px;top:12px" width="110" height="16" aria-hidden="true">
      <g fill="#fff"><circle cx="6" cy="7" r="4.5"/><circle cx="18" cy="7" r="4.5"/><circle cx="30" cy="7" r="4.5"/><circle cx="42" cy="7" r="4.5"/><circle cx="54" cy="7" r="4.5"/></g>
      <g fill="none" stroke="#fff" stroke-width="2.4" stroke-linecap="round">
        <path d="M70 6 Q80 -2 90 6"/><path d="M74 10 Q80 5 86 10"/>
      </g>
      <circle cx="80" cy="13" r="2" fill="#fff"/>
    </svg>
    <div class="abs status-time">9:23 PM</div>
    <div class="abs status-battery-text">100%</div>
    <svg class="abs" style="left:592px;top:11px" width="40" height="18" aria-hidden="true">
      <rect x="1" y="1" width="33" height="16" rx="3" fill="#fff"/>
      <rect x="35" y="6" width="3" height="6" rx="1" fill="#fff"/>
    </svg>
  </div>

  <header class="abs app-header">
    <svg class="abs" style="left:32px;top:27px" width="36" height="28" aria-hidden="true">
      <g stroke="#fff" stroke-width="3.5" stroke-linecap="round"><line x1="2" y1="3" x2="33" y2="3"/><line x1="2" y1="14" x2="33" y2="14"/><line x1="2" y1="25" x2="33" y2="25"/></g>
    </svg>
    <div class="abs header-title">My Profile</div>
    <div class="abs avatar" role="img" aria-label="User profile photo"></div>
  </header>

  <svg class="abs" style="left:34px;top:137px" width="30" height="30" aria-hidden="true">
    <rect x="2" y="5" width="26" height="23" rx="2" fill="none" stroke="#fff" stroke-width="2.5"/>
    <rect x="2" y="5" width="26" height="6" fill="#fff"/>
    <line x1="9" y1="1" x2="9" y2="7" stroke="#fff" stroke-width="2.5"/><line x1="21" y1="1" x2="21" y2="7" stroke="#fff" stroke-width="2.5"/>
    <g fill="#fff"><rect x="6" y="14" width="4" height="3"/><rect x="13" y="14" width="4" height="3"/><rect x="20" y="14" width="4" height="3"/><rect x="6" y="20" width="4" height="3"/><rect x="13" y="20" width="4" height="3"/><rect x="20" y="20" width="4" height="3"/></g>
  </svg>
  <div class="abs range-select">3 Month</div>
  <svg class="abs" style="left:190px;top:147px" width="22" height="14" aria-hidden="true"><path d="M1 2 L19 2 L10 11 Z" fill="#fff"/></svg>

  <svg class="abs weight-chart" style="left:0;top:0" width="640" height="600" font-family="Roboto, Arial, sans-serif">
    <defs>
      <linearGradient id="areaFill" x1="0" y1="0" x2="0" y2="1">
        <stop offset="0" stop-color="var(--chart-fill-top)"/>
        <stop offset="0.55" stop-color="var(--chart-fill-bottom)"/>
        <stop offset="1" stop-color="var(--app-green)" stop-opacity="0.2"/>
      </linearGradient>
    </defs>
    <path d="M76 423 C95 400 105 390 123 382 C150 365 170 345 230 330 C280 322 330 320 363 318 C420 314 480 300 510 270 C525 258 535 240 553 210 L560 210 L560 575 L76 575 Z" fill="url(#areaFill)" opacity="0.9"/>
    <g stroke="var(--grid-line)" stroke-width="1.5">
      <line x1="22" y1="215" x2="598" y2="215"/><line x1="22" y1="295" x2="598" y2="295"/><line x1="22" y1="375" x2="598" y2="375"/>
    </g>
    <g stroke="var(--grid-line)" stroke-width="1.5" stroke-dasharray="12 8">
      <line x1="76" y1="225" x2="76" y2="455"/><line x1="130" y1="225" x2="130" y2="455"/><line x1="185" y1="225" x2="185" y2="455"/><line x1="240" y1="225" x2="240" y2="455"/><line x1="295" y1="225" x2="295" y2="455"/><line x1="400" y1="225" x2="400" y2="455"/><line x1="455" y1="225" x2="455" y2="455"/><line x1="510" y1="225" x2="510" y2="455"/>
    </g>
    <g stroke="#fff" stroke-width="1.5">
      <line x1="50" y1="185" x2="50" y2="485"/><line x1="22" y1="455" x2="598" y2="455"/>
      <line x1="363" y1="185" x2="363" y2="470" stroke-width="2"/>
    </g>
    <g fill="var(--yellow)">
      <rect x="180" y="348" width="12" height="107"/><rect x="286" y="322" width="12" height="133"/>
      <rect x="394" y="312" width="12" height="143"/><rect x="504" y="275" width="12" height="180"/>
    </g>
    <path d="M76 423 C95 400 105 390 123 382 C150 365 170 345 230 330 C280 322 330 320 363 318 C420 314 480 300 510 270 C525 258 535 240 553 210" fill="none" stroke="#fff" stroke-width="2"/>
    <circle cx="123" cy="382" r="6.5" fill="#fff"/>
    <circle cx="363" cy="318" r="6.5" fill="#fff"/>
    <line x1="534" y1="188" x2="534" y2="250" stroke="#fff" stroke-width="2"/>
    <path d="M534 188 L584 188 L570 207 L584 226 L534 226 Z" fill="var(--flag-lime)"/>
    <circle cx="534" cy="251" r="6" fill="var(--goal-red)"/>
    <g fill="#fff" font-size="18">
      <text x="25" y="237">3</text><text x="25" y="317">2</text><text x="25" y="397">1</text>
      <text x="320" y="292" text-anchor="middle">54kg</text>
      <text x="76" y="492" text-anchor="middle">0</text><text x="186" y="492" text-anchor="middle">20</text>
      <text x="294" y="492" text-anchor="middle">40</text><text x="400" y="492" text-anchor="middle">60</text>
      <text x="568" y="492" text-anchor="middle" font-size="22">Weight</text>
    </g>
  </svg>

  <div class="abs stat-card" style="left:26px"><div class="stat-value">54 <span class="stat-unit">kg</span></div><div class="stat-label">weight</div></div>
  <div class="abs stat-card" style="left:236px"><div class="stat-value">167 <span class="stat-unit">cm</span></div><div class="stat-label">height</div></div>
  <div class="abs stat-card" style="left:446px"><div class="stat-value">31.2 <span class="stat-unit">%</span></div><div class="stat-label">fat</div></div>

  <div class="abs section-title" style="left:25px;top:713px">Calorie Breakdown</div>

  <div class="abs macro-label" style="left:38px;top:777px">Protein</div>
  <div class="abs macro-pct" style="left:198px;top:777px">35%</div>
  <div class="abs macro-track" style="top:816px"><div class="macro-fill" style="width:84px;background:var(--protein)"></div></div>

  <div class="abs macro-label" style="left:43px;top:849px">Carbs</div>
  <div class="abs macro-pct" style="left:198px;top:849px">47%</div>
  <div class="abs macro-track" style="top:888px"><div class="macro-fill" style="width:103px;background:var(--carbs)"></div></div>

  <div class="abs macro-label" style="left:36px;top:919px">Entergy</div>
  <div class="abs macro-pct" style="left:198px;top:919px">80%</div>
  <div class="abs macro-track" style="top:958px"><div class="macro-fill" style="width:164px;background:var(--energy)"></div></div>

  <div class="abs macro-label" style="left:43px;top:991px">Water</div>
  <div class="abs macro-pct" style="left:198px;top:991px">87%</div>
  <div class="abs macro-track" style="top:1030px"><div class="macro-fill" style="width:184px;background:var(--water)"></div></div>

  <svg class="abs calorie-pie" style="left:0;top:0" width="640" height="1100" aria-label="Calorie breakdown pie chart">
    <circle cx="471" cy="906" r="133" fill="#fff"/>
    <g stroke="#fff" stroke-width="4" stroke-linejoin="round">
      <path d="M470 912 L466.4 775.1 A131 131 0 0 1 564.6 814.3 Z" fill="var(--pie-orange)"/>
      <path d="M470 912 L564.6 814.3 A131 131 0 0 1 586.1 968.5 Z" fill="var(--pie-yellow)"/>
      <path d="M470 912 L586.1 968.5 A131 131 0 0 1 381.7 995.3 Z" fill="var(--pie-pink)"/>
      <path d="M470 912 L381.7 995.3 A131 131 0 0 1 466.4 775.1 Z" fill="var(--pie-blue)"/>
    </g>
  </svg>

  <div class="abs divider"></div>

  <div class="abs section-title" style="left:26px;top:1136px">Aims</div>

  <div class="abs aim-label" style="top:1196px">Lose&nbsp; 5 kg weight</div>
  <div class="abs aim-label" style="top:1256px">Lose&nbsp; 2 percent fat</div>
  <svg class="abs aim-sliders" style="left:0;top:1180px" width="640" height="120" aria-hidden="true">
    <line x1="286" y1="31" x2="601" y2="31" stroke="#fff" stroke-width="3"/>
    <line x1="286" y1="31" x2="366" y2="31" stroke="var(--yellow)" stroke-width="3"/>
    <circle cx="366" cy="31" r="17" fill="var(--yellow)"/>
    <line x1="286" y1="91" x2="601" y2="91" stroke="#fff" stroke-width="3"/>
    <line x1="286" y1="91" x2="486" y2="91" stroke="var(--yellow)" stroke-width="3"/>
    <circle cx="486" cy="91" r="17" fill="var(--yellow)"/>
  </svg>

</main>
</body>
</html>
```